Stationery Design Project for Wellmind Therapy Institute

I would like you to design a letterhead and appt cards and letterhead. i have attached our current brochure so that you can see the kind of clinic that we are - for some context.

Generally our letters will go to General Practitioners.
Appt cards to clients. The text can stay the same as current documents as attached but the design obviously needs to be totally changed.

We are a psychology clinic with several psychologists that work for me. THe psychologists come and go so I am not wanting to list their names on the stationary.

In terms of letterhead my name (dr marianne pelko) needs to be on there..eg dr marianne pelko & associates.

With envelopes we need to be discrete therefore we simply have WTI & our address.

Everything goes under the banner of Wellmind Therapy Institute Pty Ltd.

I would like it to be consistent in theme/colours with the logo you designed and our website which has just gone live www.wellmindtherapyinstitute.com.au

Target Market(s)

General practitioners, potential referrers usually in the medical/health field,

Industry/Entity Type

Clinic

Requirements
Must have
• Logo

Address Suite 4, 2187 Farrowby Rd, Tillermont West 3172
P 9563 2814 F 9563 2816 E info@wellmindtherapyinstitute.com.au
W wellmindtherapyinstitute.com.au

Wellmind Therapy Institute Pty Ltd (small font)
ABN (ill need to provide this) (small font)
Nice to have
• I really like in my website how the colours are graded in the banners...I think this gives a softer feel...so if something like that would look good in our stationary then please use that kind of technique too...but you guys are the experts.

```html
<!DOCTYPE html>
<html lang="en">
<head>
<meta charset="utf-8">
<title>Wellmind Therapy Institute — Stationery</title>
<link rel="stylesheet" href="https://fonts.googleapis.com/css2?family=Arimo:ital,wght@0,400;0,700;1,400&display=swap">
<style>
  :root {
    --teal: #0fb3b5;
    --teal-deep: #0a9a9c;
    --teal-light: #2cc6c6;
    --paper: #ffffff;
    --ink: #1c1c1c;
    --ink-soft: #555555;
    --field-line: #c9c9c9;
    --field-text: #c4c4c4;
    --backdrop: #e9ecec;
  }
  * { box-sizing: border-box; margin: 0; padding: 0; }
  html, body { width: 1200px; height: 996px; overflow: hidden; }
  body {
    background: var(--backdrop);
    font-family: "Arimo", Arial, sans-serif;
    position: relative;
  }
  .sheet { position: absolute; overflow: hidden; box-shadow: 0 2px 10px rgba(0,0,0,.12); }

  /* brand lockup */
  .brand { position: absolute; display: flex; align-items: center; gap: 9px; color: var(--paper); }
  .brand-dot { width: 26px; height: 26px; border-radius: 50%; background: var(--paper); flex: none; }
  .brand-name { font-size: 9.5px; font-weight: 400; letter-spacing: 2.2px; line-height: 12px; text-transform: uppercase; }
  .brand-lg .brand-dot { width: 38px; height: 38px; }
  .brand-lg .brand-name { font-size: 12px; letter-spacing: 2.6px; line-height: 14px; }

  /* business card */
  .business-card {
    left: 32px; top: 114px; width: 284px; height: 466px;
    background: linear-gradient(160deg, var(--teal-light) 0%, var(--teal) 45%, var(--teal-deep) 100%);
  }
  .business-card .brand { left: 61px; top: 176px; }
  .card-contact { position: absolute; left: 52px; top: 370px; color: var(--paper); font-size: 10px; line-height: 12.5px; }
  .card-contact b { font-weight: 700; }

  /* appointment card */
  .appointment-card { left: 332px; top: 114px; width: 284px; height: 466px; background: var(--paper); }
  .appointment-card .top-band { position: absolute; left: 0; top: 0; }
  .appointment-card .brand { left: 36px; top: 32px; }
  .field-label { position: absolute; left: 36px; font-size: 10px; font-weight: 700; color: var(--ink); }
  .psychologist-box { position: absolute; left: 127px; top: 136px; width: 126px; height: 21px; border: 1.5px solid var(--field-line); border-radius: 2px; }
  .slot-row { position: absolute; left: 42px; display: flex; align-items: center; gap: 4px; font-size: 9.5px; color: var(--ink-soft); }
  .slot-row .row-label { width: 30px; }
  .slot { width: 21px; height: 21px; border: 1.5px solid var(--field-line); border-radius: 2px; font-size: 9px; color: var(--field-text); display: flex; align-items: center; justify-content: center; }
  .slot-sep { width: 6px; text-align: center; color: var(--ink-soft); }
  .fee-note { position: absolute; left: 40px; top: 392px; width: 220px; font-size: 9.5px; font-style: italic; line-height: 13px; color: var(--ink-soft); }

  /* letterhead */
  .letterhead { left: 629px; top: 114px; width: 533px; height: 752px; background: var(--paper); }
  .letterhead .top-band { position: absolute; left: 0; top: 0; }
  .letterhead .brand { left: 338px; top: 26px; }
  .letter-sender { position: absolute; left: 50px; top: 38px; font-size: 8px; line-height: 11px; color: var(--ink); }
  .letter-sender b { font-weight: 700; }

  /* envelope */
  .envelope {
    left: 40px; top: 605px; width: 573px; height: 271px;
    background: linear-gradient(170deg, var(--teal-light) 0%, var(--teal) 50%, var(--teal-deep) 100%);
  }
  .envelope .soft-glow { position: absolute; left: 380px; top: 10px; width: 240px; height: 240px; border-radius: 50%; background: rgba(255,255,255,.07); }
  .envelope .brand { left: 420px; top: 112px; }
  .recipient { position: absolute; left: 23px; top: 41px; font-size: 10px; line-height: 11.5px; color: var(--paper); }
  .recipient b { font-weight: 700; }
</style>
</head>
<body>

  <section class="sheet business-card">
    <div class="brand brand-lg">
      <span class="brand-dot"></span>
      <span class="brand-name">Wellmind<br>Therapy<br>Institute</span>
    </div>
    <div class="card-contact">
      <b>Wellmind Therapy Institute Pty Ltd</b><br>
      Suite 4, 2187 Farrowby Rd, Tillermont West 3172<br>
      <b>Phone:</b> 9563 2814 <b>Fax</b> 9563 2816<br>
      info@wellmindtherapyinstitute.com.au
    </div>
  </section>

  <section class="sheet appointment-card">
    <svg class="top-band" width="284" height="110" viewBox="0 0 284 110" aria-hidden="true">
      <path d="M0 0 H284 V36 C190 30 120 112 0 108 Z" fill="var(--teal)"/>
    </svg>
    <div class="brand">
      <span class="brand-dot"></span>
      <span class="brand-name">Wellmind<br>Therapy<br>Institute</span>
    </div>

    <div class="field-label" style="top:141px">Your psychologist:</div>
    <div class="psychologist-box"></div>
    <div class="field-label" style="top:166px">Your appointments:</div>

    <div class="slot-row" style="top:186px"><span class="row-label">Date :</span><span class="slot">Y</span><span class="slot">Y</span><span class="slot">M</span><span class="slot">M</span><span class="slot">D</span><span class="slot">D</span></div>
    <div class="slot-row" style="top:214px"><span class="row-label">Time :</span><span class="slot">h</span><span class="slot">h</span><span class="slot-sep">:</span><span class="slot">m</span><span class="slot">m</span></div>

    <div class="slot-row" style="top:252px"><span class="row-label">Date :</span><span class="slot">Y</span><span class="slot">Y</span><span class="slot">M</span><span class="slot">M</span><span class="slot">D</span><span class="slot">D</span></div>
    <div class="slot-row" style="top:280px"><span class="row-label">Time :</span><span class="slot">h</span><span class="slot">h</span><span class="slot-sep">:</span><span class="slot">m</span><span class="slot">m</span></div>

    <div class="slot-row" style="top:313px"><span class="row-label">Date :</span><span class="slot">Y</span><span class="slot">Y</span><span class="slot">M</span><span class="slot">M</span><span class="slot">D</span><span class="slot">D</span></div>
    <div class="slot-row" style="top:341px"><span class="row-label">Time :</span><span class="slot">h</span><span class="slot">h</span><span class="slot-sep">:</span><span class="slot">m</span><span class="slot">m</span></div>

    <p class="fee-note">Please note fees will be charged for missing appointments without 48 hour notice</p>
  </section>

  <section class="sheet letterhead">
    <svg class="top-band" width="533" height="140" viewBox="0 0 533 140" aria-hidden="true">
      <rect x="295" y="0" width="238" height="66" fill="var(--teal)"/>
      <circle cx="397" cy="36" r="102" fill="var(--teal)"/>
    </svg>
    <div class="brand">
      <span class="brand-dot"></span>
      <span class="brand-name">Wellmind<br>Therapy<br>Institute</span>
    </div>
    <div class="letter-sender">
      <b>Wellmind Therapy Institute Pty Ltd</b><br>
      Suite 4, 2187 Farrowby Rd, Tillermont West 3172<br>
      <b>Phone:</b> 9563 2814 <b>Fax</b> 9563 2816<br>
      info@wellmindtherapyinstitute.com.au
    </div>
  </section>

  <section class="sheet envelope">
    <div class="soft-glow"></div>
    <div class="recipient">
      <b>Name Surname</b>, Company<br>
      City, State, Country, Zip
    </div>
    <div class="brand">
      <span class="brand-dot"></span>
      <span class="brand-name">Wellmind<br>Therapy<br>Institute</span>
    </div>
  </section>

</body>
</html>
```